Business Card Design Project

Business Card
We are rebranding with a new logo
Industry/Entity Type
Business
Contact Information for Business Card
Dennis Marlow +61 427581962 dennis@qovo.com.au P.O. Box 872 Kelvindale QLD 4309
Requirements
Must have
- Logo

```html
<!DOCTYPE html>
<html lang="en">
<head>
<meta charset="UTF-8">
<title>Qovo International – Business Card</title>
<link href="https://fonts.googleapis.com/css2?family=Source+Sans+3:wght@400;600&display=swap" rel="stylesheet">
<style>
  :root {
    --bg: #e9ebee;
    --navy: #17577c;
    --deep: #1c6a96;
    --sky: #23a0d8;
    --orange: #f28a1e;
    --orange-red: #e8601c;
    --white: #ffffff;
  }
  html, body {
    margin: 0;
    width: 1200px;
    height: 800px;
    overflow: hidden;
    background: var(--bg);
    font-family: "Source Sans 3", "Myriad Pro", sans-serif;
  }
  .card {
    position: absolute;
    left: 150px;
    top: 143px;
    width: 900px;
    height: 514px;
    box-shadow: 0 12px 30px rgba(0,0,0,0.18);
    overflow: hidden;
  }
  .card-art {
    position: absolute;
    inset: 0;
  }
  .brand-name {
    position: absolute;
    left: 95px;
    top: 205px;
    width: 240px;
    text-align: center;
    color: var(--navy);
    font-weight: 600;
    font-size: 25px;
    line-height: 40px;
  }
  .holder-name {
    position: absolute;
    left: 505px;
    top: 92px;
    color: var(--white);
    font-weight: 400;
    font-size: 36px;
    letter-spacing: 0.3px;
  }
  .contact-list {
    position: absolute;
    left: 495px;
    top: 180px;
    margin: 0;
    padding: 0;
    list-style: none;
  }
  .contact-item {
    display: flex;
    align-items: center;
    height: 46px;
    margin-bottom: 24px;
    color: var(--white);
    font-size: 21px;
  }
  .contact-icon {
    width: 44px;
    height: 40px;
    margin-right: 22px;
    flex: none;
  }
</style>
</head>
<body>
  <div class="card">
    <svg class="card-art" width="900" height="514" viewBox="0 0 900 514">
      <defs>
        <linearGradient id="panel-shade" x1="0" y1="0" x2="1" y2="1">
          <stop offset="0" stop-color="#1b6e9c"/>
          <stop offset="1" stop-color="#15506f"/>
        </linearGradient>
      </defs>
      <rect class="card-base" width="900" height="514" fill="var(--deep)"/>
      <rect class="info-panel" width="900" height="514" fill="url(#panel-shade)"/>
      <polygon class="left-field" points="0,0 260,0 120,514 0,514" fill="var(--deep)"/>
      <polygon class="sky-band" points="312,0 540,0 400,514 172,514" fill="var(--sky)"/>
      <polygon class="stripe sky-line" points="260,0 268,0 128,514 120,514" fill="var(--sky)"/>
      <polygon class="stripe orange-red" points="270,0 284,0 144,514 130,514" fill="var(--orange-red)"/>
      <polygon class="stripe sky-line" points="286,0 294,0 154,514 146,514" fill="var(--sky)"/>
      <polygon class="stripe orange" points="296,0 312,0 172,514 156,514" fill="var(--orange)"/>
      <g class="logo-badge">
        <polygon points="347,225 281,339 149,339 83,225 149,111 281,111" fill="var(--sky)"/>
        <polygon points="333,225 274,327 156,327 97,225 156,123 274,123" fill="var(--white)"/>
        <polygon points="322,225 268,318 162,318 108,225 162,132 268,132" fill="none" stroke="var(--sky)" stroke-width="2"/>
      </g>
    </svg>

    <div class="brand-name">Qovo International</div>

    <div class="holder-name">Dennis Marlow</div>

    <ul class="contact-list">
      <li class="contact-item">
        <svg class="contact-icon" viewBox="0 0 44 40" aria-hidden="true">
          <polygon points="44,20 33,39 11,39 0,20 11,1 33,1" fill="var(--white)"/>
          <path d="M16 11 l4 0 2 5 -3 2 q2 5 6 6 l2 -3 5 2 0 4 q-1 2 -4 2 q-13 -2 -14 -14 q0 -3 2 -4z" fill="var(--deep)"/>
        </svg>
        <span>+61 427581962</span>
      </li>
      <li class="contact-item">
        <svg class="contact-icon" viewBox="0 0 44 40" aria-hidden="true">
          <polygon points="44,20 33,39 11,39 0,20 11,1 33,1" fill="var(--white)"/>
          <rect x="11" y="13" width="22" height="15" fill="var(--deep)"/>
          <polyline points="11,13 22,22 33,13" fill="none" stroke="var(--white)" stroke-width="2"/>
        </svg>
        <span>dennis@qovo.com.au</span>
      </li>
      <li class="contact-item">
        <svg class="contact-icon" viewBox="0 0 44 40" aria-hidden="true">
          <polygon points="44,20 33,39 11,39 0,20 11,1 33,1" fill="var(--white)"/>
          <path d="M22 31 q-8 -9 -8 -14 a8 8 0 0 1 16 0 q0 5 -8 14z" fill="var(--deep)"/>
          <circle cx="22" cy="17" r="3" fill="var(--white)"/>
        </svg>
        <span>P.O. Box 872 - Kelvindale QLD 4309</span>
      </li>
    </ul>
  </div>
</body>
</html>
```